Need new Spot UV Business Card design

We are looking for a new business card design incorporating Spot UV in black & white options / versions. See examples files and Tobin Ashgrove Design logo.
You can see our website at www.tobinashgrove.ca. We want something classy but yet modern. We are open to black or black and/or white on white with the spot uv. We are open to portrait or landscape. Size should be standard 3.5" x 2". The front of the card should focus on the logo and name "Tobin Ashgrove" only. Fonts used should be "Open sans" or "PT Sans".

Target Market(s)

Mid to high end

Industry/Entity Type

Business

Contact Information for Business Card

Tobin Velasko
416.382.4417
tobin@tobinashgrove.ca
www.tobinashgrove.ca
4175 Brightwell Blvd. E Suite 308
Mississauga, ON L5T 2K9

Requirements
Must have
• Name & Logo

```html
<!DOCTYPE html>
<html lang="en">
<head>
<meta charset="utf-8">
<title>Tobin Ashgrove — Business Card</title>
<link href="https://fonts.googleapis.com/css2?family=Open+Sans:wght@300;400;700&display=swap" rel="stylesheet">
<style>
  :root {
    --bg-light: #f2f2f2;
    --bg-shade: #c9c9c9;
    --card-black: #0b0b0b;
    --card-edge: #1c1c1c;
    --silver: #d8d8d8;
    --silver-dim: #a9a9a9;
    --uv-faint: rgba(255, 255, 255, 0.10);
    --text-white: #ffffff;
    --text-grey: #bdbdbd;
  }
  * { box-sizing: border-box; margin: 0; padding: 0; }
  html, body { width: 1200px; height: 900px; overflow: hidden; }
  body {
    font-family: "Open Sans", sans-serif;
    background: radial-gradient(ellipse at 70% 30%, var(--bg-light) 0%, #e4e4e4 55%, var(--bg-shade) 100%);
    position: relative;
  }
  .card {
    position: absolute;
    width: 600px;
    height: 343px;
    background: linear-gradient(135deg, var(--card-edge) 0%, var(--card-black) 45%, #050505 100%);
    border-radius: 3px;
    box-shadow: 0 18px 40px rgba(0,0,0,0.35);
    overflow: hidden;
  }
  .card--front { left: 110px; top: 90px; }
  .card--back { left: 490px; top: 470px; }

  /* Front */
  .uv-square {
    position: absolute;
    left: -40px;
    top: 70px;
    width: 300px;
    height: 300px;
    border: 14px solid var(--uv-faint);
  }
  .front-brand {
    position: absolute;
    left: 230px;
    top: 148px;
    display: flex;
    align-items: center;
    gap: 16px;
  }
  .brand-square {
    width: 46px;
    height: 46px;
    border: 3px solid var(--silver);
  }
  .brand-name {
    font-family: "Open Sans", sans-serif;
    font-weight: 300;
    font-size: 30px;
    letter-spacing: 1px;
    color: var(--silver);
    text-transform: uppercase;
  }

  /* Back */
  .back-mark {
    position: absolute;
    left: 70px;
    top: 86px;
    width: 170px;
    height: 170px;
    border: 6px solid var(--silver);
    display: flex;
    align-items: center;
    justify-content: center;
  }
  .back-mark__name {
    font-weight: 300;
    font-size: 19px;
    line-height: 1.25;
    color: var(--silver);
    text-align: center;
    text-transform: uppercase;
    letter-spacing: 1px;
  }
  .contact {
    position: absolute;
    right: 34px;
    top: 54px;
    text-align: right;
    color: var(--text-grey);
  }
  .contact__name {
    font-weight: 700;
    font-size: 23px;
    color: var(--text-white);
    line-height: 1.1;
  }
  .contact__title {
    font-size: 13px;
    color: var(--text-grey);
    margin-bottom: 12px;
  }
  .contact__address {
    font-size: 14px;
    line-height: 1.35;
  }
  .contact-list {
    position: absolute;
    right: 34px;
    bottom: 42px;
    list-style: none;
    text-align: right;
  }
  .contact-list li {
    display: flex;
    align-items: center;
    justify-content: flex-end;
    gap: 10px;
    font-size: 15px;
    line-height: 1.45;
    color: var(--text-white);
  }
  .contact-list svg { width: 13px; height: 13px; fill: none; stroke: var(--text-white); stroke-width: 1.6; }
</style>
</head>
<body>

  <section class="card card--front" aria-label="Card front">
    <div class="uv-square"></div>
    <div class="front-brand">
      <div class="brand-square"></div>
      <span class="brand-name">Tobin Ashgrove</span>
    </div>
  </section>

  <section class="card card--back" aria-label="Card back">
    <div class="back-mark">
      <span class="back-mark__name">Tobin<br>Ashgrove</span>
    </div>
    <div class="contact">
      <p class="contact__name">Tobin Velasko</p>
      <p class="contact__title">Managing Member</p>
      <p class="contact__address">4175 Brightwell Blvd. E Suite 308<br>Mississauga, ON L5T 2K9</p>
    </div>
    <ul class="contact-list">
      <li>416.382.4417
        <svg viewBox="0 0 16 16" aria-hidden="true"><path d="M3 2l3 0 1 3-2 1.5c1 2 2.5 3.5 4.5 4.5L11 9l3 1v3c-6 0-11-5-11-11z"/></svg>
      </li>
      <li>tobin@tobinashgrove.ca
        <svg viewBox="0 0 16 16" aria-hidden="true"><rect x="1.5" y="3.5" width="13" height="9"/><path d="M1.5 3.5l6.5 5 6.5-5"/></svg>
      </li>
      <li>www.tobinashgrove.ca
        <svg viewBox="0 0 16 16" aria-hidden="true"><circle cx="8" cy="8" r="6.5"/><ellipse cx="8" cy="8" rx="3" ry="6.5"/><path d="M1.5 8h13"/></svg>
      </li>
    </ul>
  </section>

</body>
</html>
```